Family history tech product tailored for moms needs banner ads

lumeo.com is launching next week and we've partnered with an ad group that will be launching a campaign on school district websites that will be pushed to 250k moms of school age children.

We're launching a $199 product that shows you more about who you are through your family's history. We connect people wanting to learn more about themselves with expert researcher/genealogist who will uncover their past and find the stories of their ancestors.

See branding guidelines below as well as the landing page we're designing where these ads will take you.

Here is the landing page design:
https://quillshare-files.net/K038HM2R4-G46T6TFDD0-ee1d3bce78

Target Market(s)

Mom's of kids in elementary and middle school.

Persona:
Mom, 38 years old, 2 kids (age 6 and 8)
Lives in Dallas, drives a 2016 Varno Keldra
She and husband met in college. She was a nurse, but she stopped working to be a full-time mom
Husband is in financial consulting, household income of $140,000
When kids at school, she runs errands, works out, meets up with girlfriends for coffee
She shops at Zintavo, has active hobbies
She is always busy, there’s not enough time for her family; she is worried that her kids may become distant because of how busy the family is
She values time with family most, soccer weekends, financial stability, college for the kids
Wants to connect more with the kids and the family to increase the bond, and she thinking having more context for the family will help them bond around a common history
Her objections to Tavenry are lack of trust in a new service, time it will cost her to get the info she wants to achieve her goals

Industry/Entity Type

Startup

Other font styles liked:
• follow style guide

Requirements
Must have
• Must follow the design pattern in our branding guide.
• https://www.boxhaven-example.net/s/qrt4jwk313mzkpa/Screenshot%202016-11-30%2013.39.48.png?dl=0
Nice to have
• Good copy, I'm less worried about that though. We can work together on that.
Should not have
• Stock imagery that sucks. I'm really opposed to anything that looks like it is from the 2001 - 2011

```html
<!DOCTYPE html>
<html lang="en">
<head>
<meta charset="utf-8">
<title>Tavenry – Find yours</title>
<link rel="stylesheet" href="https://fonts.googleapis.com/css2?family=Open+Sans:wght@400;600;700&display=swap">
<style>
  :root {
    --bg: #ffffff;
    --pattern-blue: #dcebfb;
    --brand-blue: #2f95f0;
    --heading: #3b5368;
    --teal-deep: #1599a3;
    --teal-light: #48cad7;
    --shadow-grey: #d3d6d6;
    --skin-light: #f6d3bb;
    --skin-mid: #eeaa8c;
    --white: #ffffff;
  }
  * { margin: 0; padding: 0; box-sizing: border-box; }
  html, body { width: 1200px; height: 1000px; overflow: hidden; background: var(--bg); }
  body { font-family: "Open Sans", Arial, sans-serif; }

  .banner { position: relative; width: 1200px; height: 1000px; overflow: hidden; background: var(--bg); }

  .backdrop-pattern {
    position: absolute; inset: 0;
    background: linear-gradient(120deg, var(--pattern-blue) 0%, rgba(220,235,251,0.55) 40%, rgba(255,255,255,0) 75%);
  }

  .brand {
    position: absolute; top: 44px; right: 56px;
    display: flex; flex-direction: column; align-items: center; gap: 10px;
  }
  .brand-dot { width: 72px; height: 72px; border-radius: 50%; background: var(--brand-blue); }
  .brand-name { font-weight: 700; font-size: 38px; line-height: 1; color: var(--brand-blue); letter-spacing: -0.5px; }

  .headline { position: absolute; left: 0; top: 0; color: var(--heading); font-weight: 700; font-size: 68px; letter-spacing: -1.2px; line-height: 1; white-space: nowrap; }
  .headline-line { position: absolute; }
  .headline-line.first { left: 104px; top: 196px; }
  .headline-line.second { left: 344px; top: 287px; }

  .cta { position: absolute; }
  .cta-shadow { position: absolute; background: var(--shadow-grey); }
  .cta-box { position: absolute; display: flex; align-items: center; color: var(--white); white-space: nowrap; }

  .cta-primary .cta-shadow { left: 578px; top: 446px; width: 586px; height: 146px; }
  .cta-primary .cta-box { left: 555px; top: 425px; width: 585px; height: 141px; background: var(--teal-deep); justify-content: center; font-weight: 700; font-size: 86px; letter-spacing: -0.5px; padding-bottom: 6px; }

  .tagline .cta-shadow { left: 595px; top: 748px; width: 605px; height: 130px; }
  .tagline .cta-box { left: 569px; top: 722px; width: 631px; height: 132px; background: var(--teal-light); padding-left: 42px; font-weight: 400; font-size: 41px; letter-spacing: 6.8px; }

  .hands-photo {
    position: absolute; left: 38px; top: 410px; width: 482px; height: 590px;
    border-radius: 200px 200px 0 0;
    background: radial-gradient(ellipse at 50% 55%, var(--skin-light) 0%, var(--skin-mid) 70%, rgba(238,170,140,0) 100%);
  }
</style>
</head>
<body>
  <main class="banner">
    <div class="backdrop-pattern" role="img" aria-label="Decorative pattern of light blue diagonal rounded dashes"></div>

    <div class="brand">
      <span class="brand-dot"></span>
      <span class="brand-name">tavenry</span>
    </div>

    <h1 class="headline">
      <span class="headline-line first">Everyone has a story...</span>
      <span class="headline-line second">A unique family story ...</span>
    </h1>

    <div class="hands-photo" role="img" aria-label="Photo of a child's open hand pressed against an adult's open hand"></div>

    <div class="cta cta-primary">
      <div class="cta-shadow"></div>
      <div class="cta-box">Find yours</div>
    </div>

    <div class="cta tagline">
      <div class="cta-shadow"></div>
      <div class="cta-box">Yourself, Discovered.</div>
    </div>
  </main>
</body>
</html>
```